Create Lanternfield HR Business Cards.

Create Business Cards for Lanternfield HR. 2 sided and Would like the back to have the logo.

Info for Business Card:
Address: 4827 Millbrook Ave Suite 230 Cleveland, Ohio 44987
Office Number: 216-555-0143
Mobile: 216-555-0192

Website: www.lanternfieldhr.example

Target Market(s)

Small to medium size businesses

Industry/Entity Type

Human Resources

Contact Information for Business Card

Company logo and information

Font styles to use
Serif
Sans Serif

Requirements
Must have
• Info for Business Card: Address: 4827 Millbrook Ave Suite 230 Cleveland, Ohio 44987 Office Number: 216-555-0143 Mobile: 216-555-0192 Website: www.lanternfieldhr.example

```html
<!DOCTYPE html>
<html lang="en">
<head>
<meta charset="utf-8">
<title>Lanternfield HR Business Cards</title>
<link rel="stylesheet" href="https://fonts.googleapis.com/css2?family=Poppins:wght@600&family=Open+Sans:wght@400&display=swap">
<style>
  :root {
    --navy: #262262;
    --orange: #f7890b;
    --paper: #f4f4f4;
    --stage: #b3b3b3;
    --ink: #231f20;
    --white: #ffffff;
  }
  html, body {
    margin: 0;
    width: 1200px;
    height: 1200px;
    overflow: hidden;
    background: var(--stage);
  }
  .card {
    position: absolute;
    left: 215px;
    width: 769px;
    height: 452px;
    background: var(--paper);
    overflow: hidden;
  }
  .card--front { top: 83px; }
  .card--back { top: 619px; }
  .card__art {
    position: absolute;
    inset: 0;
    width: 100%;
    height: 100%;
  }
  .brand {
    position: absolute;
    display: flex;
    align-items: center;
    font-family: "Poppins", sans-serif;
    font-weight: 600;
    color: var(--navy);
    white-space: nowrap;
  }
  .brand__dot {
    border-radius: 50%;
    background: var(--orange);
    flex: none;
  }
  .brand--front {
    left: 0;
    right: 0;
    top: 280px;
    justify-content: center;
    font-size: 50px;
    gap: 16px;
  }
  .brand--front .brand__dot { width: 42px; height: 42px; }
  .brand--back {
    left: 120px;
    top: 326px;
    font-size: 23px;
    gap: 9px;
  }
  .brand--back .brand__dot { width: 20px; height: 20px; }
  .divider {
    position: absolute;
    left: 339px;
    top: 235px;
    width: 2px;
    height: 193px;
    background: #c9c9c9;
  }
  .contact {
    position: absolute;
    left: 416px;
    font-family: "Open Sans", sans-serif;
    font-size: 16.5px;
    line-height: 23px;
    color: var(--ink);
    margin: 0;
  }
  .contact--phone { top: 232px; }
  .contact--address { top: 295px; }
  .contact--web { top: 368px; }
</style>
</head>
<body>

<section class="card card--front" aria-label="Card front">
  <svg class="card__art" viewBox="0 0 641 377" preserveAspectRatio="none" aria-hidden="true">
    <path fill="var(--orange)" d="M0,30 C120,55 250,95 360,72 C430,58 500,48 555,75 C600,98 625,140 641,182 L641,186 C615,140 585,112 540,100 C480,86 420,92 360,102 C250,122 120,110 0,70 Z"/>
    <path fill="var(--navy)" stroke="var(--white)" stroke-width="9" d="M-10,-10 H651 V186 C628,128 600,84 558,62 C500,34 420,44 360,54 C250,74 120,40 -10,14 Z"/>
  </svg>
  <div class="brand brand--front">
    <span class="brand__dot"></span>
    <span class="brand__name">Lanternfield HR</span>
  </div>
</section>

<section class="card card--back" aria-label="Card back">
  <svg class="card__art" viewBox="0 0 641 377" preserveAspectRatio="none" aria-hidden="true">
    <path fill="var(--orange)" d="M572,0 H606 C540,92 430,142 320,160 C200,180 105,218 76,292 C64,322 62,350 64,377 H58 C52,345 52,305 62,275 C88,198 172,152 300,138 C400,126 500,84 572,0 Z"/>
    <path fill="var(--navy)" stroke="var(--white)" stroke-width="8" d="M-10,-10 H568 C502,78 402,118 300,132 C178,150 88,196 60,276 C50,310 52,345 58,387 H-10 Z"/>
  </svg>

  <div class="brand brand--back">
    <span class="brand__dot"></span>
    <span class="brand__name">Lanternfield HR</span>
  </div>

  <div class="divider"></div>

  <svg class="card__art" viewBox="0 0 769 452" aria-hidden="true">
    <g class="icon icon--phone">
      <circle cx="381" cy="254" r="15" fill="var(--navy)"/>
      <rect x="376" y="245" width="10" height="18" rx="2" fill="none" stroke="var(--white)" stroke-width="1.8"/>
      <circle cx="381" cy="259.5" r="1.2" fill="var(--white)"/>
    </g>
    <g class="icon icon--pin">
      <circle cx="381" cy="320" r="15" fill="var(--orange)"/>
      <path d="M381,329 C377,323 375,319.5 375,316.5 A6,6 0 0 1 387,316.5 C387,319.5 385,323 381,329 Z" fill="var(--white)"/>
      <circle cx="381" cy="316.5" r="2" fill="var(--orange)"/>
    </g>
    <g class="icon icon--globe" fill="none" stroke="var(--white)" stroke-width="1.3">
      <circle cx="381" cy="380" r="15" fill="var(--navy)" stroke="none"/>
      <circle cx="381" cy="380" r="6.5"/>
      <ellipse cx="381" cy="380" rx="2.8" ry="6.5"/>
      <line x1="374.5" y1="380" x2="387.5" y2="380"/>
    </g>
  </svg>

  <p class="contact contact--phone">216-555-0143<br>216-555-0192</p>
  <p class="contact contact--address">4827 Millbrook Ave Suite 230 Cleveland,<br>Ohio 44987</p>
  <p class="contact contact--web">www.lanternfieldhr.example</p>
</section>

</body>
</html>
```